Veldrun Design Template

I'd like to have a powerpoint templates. In particular a resume template design upon the Veldrun website (www.veldrun.nl). Veldrun is the overarching label in grey tones. The website is therefore more focussed on Techveldrun in blue colors, I expect more brigades in the future with different color tones.

The resume template can hopefulle reused as template for business development and more.

The template should be highly professional. Preferably with a one-pager summary in front and 2 work experience details and last page with education/certificates and competences.

The onepager master slide should include
- Profile picture
- Name
- About me (optionally to mention this literally, this text can be alongside/next to the profile picture
- Table of work experience summary

In short, age, place of living, mobile phone nr in footer?
In the workexperience it describes Role, timeframe, subtitle used in slide 1 (summary of role), with a section of scope and section for achievements.

From a visual perspective, please stick to the logos provided. You may want to grey out the logo. Keep the logo as it is and work with collor pallet
Light Grey: #DEDEDE
Medium Grey: #888888
Black: #3A3A3A

```html
<!DOCTYPE html>
<html lang="en">
<head>
<meta charset="utf-8">
<title>Veldrun Resume Template</title>
<link href="https://fonts.googleapis.com/css2?family=Poppins:wght@400;600;700&family=Roboto:wght@400;500&display=swap" rel="stylesheet">
<style>
  :root{
    --light:#DEDEDE;
    --medium:#888888;
    --black:#3A3A3A;
    --ink:#1c1c1c;
    --text:#8a8a8a;
    --white:#ffffff;
    --rule:#cfcfcf;
    --ring:#e2e2e2;
    --ring-dark:#4a4a4a;
  }
  *{box-sizing:border-box;margin:0;padding:0}
  html,body{width:731px;height:1200px;overflow:hidden}
  body{background:linear-gradient(#a9a9a9 0%,#6a6a6a 40%,#575757 100%);font-family:'Roboto',sans-serif;position:relative;-webkit-font-smoothing:antialiased;-moz-osx-font-smoothing:grayscale;text-rendering:geometricPrecision}
  .slide{position:absolute;left:60px;width:611px;height:343px;background:var(--light);box-shadow:0 10px 24px rgba(0,0,0,.35)}
  .slide--cover{top:62px}
  .slide--experience{top:429px}
  .slide--education{top:795px}
  .page-num{position:absolute;left:597px;top:332px;font-size:4.5px;color:var(--black);font-weight:500}

  /* cover */
  .brand{position:absolute;left:24px;top:18px;font-family:'Poppins',sans-serif;font-weight:400;font-size:40px;color:var(--black);letter-spacing:-.5px;line-height:1}
  .profile{position:absolute;left:0;top:79px;width:184px;height:264px;background:var(--medium);border-radius:92px 92px 0 0}
  .profile__photo{position:absolute;left:25px;top:14px;width:132px;height:132px;border-radius:50%;background:radial-gradient(circle at 50% 40%,#d8d3cc 0%,#8b8f96 55%,#4e5866 100%)}
  .profile__name{position:absolute;left:0;width:184px;top:158px;text-align:center;font-family:'Poppins',sans-serif;font-weight:700;font-size:13.5px;color:var(--light)}
  .profile__title{position:absolute;left:0;width:184px;top:177px;text-align:center;font-size:7px;color:var(--light)}
  .profile__rule{position:absolute;left:17px;width:151px;top:196px;border-top:1px solid #a2a2a2}
  .socials{position:absolute;left:0;width:184px;top:205px;display:flex;justify-content:center;gap:5px}
  .socials span{width:18.5px;height:18.5px;border-radius:50%;background:var(--white)}
  .profile__meta{position:absolute;left:0;width:184px;text-align:center;font-size:5.6px;color:var(--white)}
  .profile__meta--age{top:237px}
  .profile__meta--contact{top:247px;display:flex;justify-content:center;gap:8px;align-items:center}
  .profile__meta--contact span{display:flex;align-items:center;gap:2px}

  .card{position:absolute;background:var(--white);border:1px solid #c9c9c9;border-radius:3px}
  .card--about{left:196px;top:13px;width:402px;height:318px}
  .card--wide{left:13px;top:13px;width:585px;height:318px}
  .h{position:absolute;font-family:'Poppins',sans-serif;font-weight:700;font-size:12px;color:var(--ink);line-height:1}
  .para{position:absolute;font-size:6.5px;line-height:13.1px;color:var(--text);text-align:justify}

  .xp-table{position:absolute;left:31px;top:207px;width:339px;border-collapse:collapse;font-size:5.8px;color:var(--black)}
  .xp-table th{background:var(--medium);color:var(--white);font-weight:500;font-size:6.8px;height:22px;text-transform:uppercase;border-left:1px solid var(--white)}
  .xp-table th:first-child{border-left:none}
  .xp-table td{height:21px;border:1px solid var(--rule);text-align:center}
  .xp-table td:first-child{text-align:left;padding-left:7px}

  /* experience */
  .divider{position:absolute;left:289px;top:22px;height:273px;border-left:1px solid var(--rule)}
  .role__photo{position:absolute;left:36px;top:51px;width:49px;height:49px;border-radius:50%;background:radial-gradient(circle at 50% 40%,#d8d3cc 0%,#8b8f96 55%,#4e5866 100%)}
  .role__lines{position:absolute;left:95px;top:55px;font-size:8.4px;line-height:15px;color:var(--black)}
  .role__lines strong{font-weight:500}
  .list{position:absolute;list-style:none;font-size:7.3px;font-weight:400;color:var(--ink)}
  .list li{display:flex;align-items:center;gap:9px;height:14px;color:var(--ink)}
  .list svg{width:7px;height:7px;flex:none}
  .rings{position:absolute;left:312px;top:207px;width:265px;height:92px}
  .ring-label{position:absolute;width:70px;text-align:center;font-size:7.9px;line-height:13px;color:var(--ink);transform:translate(-50%,-50%)}

  /* education */
  .cert{position:absolute;width:105px;height:80px;background:var(--medium);border-radius:2px}
  .cert__sheet{position:absolute;left:7px;top:6px;right:7px;bottom:12px;background:linear-gradient(90deg,#bdbdbd,#f4f4f4 20%,#fafafa 80%,#bdbdbd)}
</style>
</head>
<body>

<!-- Slide 1: summary -->
<section class="slide slide--cover">
  <div class="brand">veldrun</div>
  <div class="profile">
    <div class="profile__photo" role="img" aria-label="Portrait photo of the candidate"></div>
    <div class="profile__name">John Doe</div>
    <div class="profile__title">Lorem Ipsum Dolor</div>
    <div class="profile__rule"></div>
    <div class="socials" aria-label="Social profiles"><span></span><span></span><span></span><span></span><span></span></div>
    <div class="profile__meta profile__meta--age">Age : 30Years</div>
    <div class="profile__meta profile__meta--contact">
      <span><svg width="6" height="6" viewBox="0 0 24 24"><path fill="#fff" d="M6.6 10.8a15.1 15.1 0 006.6 6.6l2.2-2.2c.3-.3.7-.4 1-.2 1.1.4 2.3.6 3.6.6.6 0 1 .4 1 1V20c0 .6-.4 1-1 1A17 17 0 013 4c0-.6.4-1 1-1h3.5c.6 0 1 .4 1 1 0 1.3.2 2.5.6 3.6.1.3 0 .7-.2 1z"/></svg>Mobile : +1 555 014 2736</span>
      <span><svg width="6" height="6" viewBox="0 0 24 24"><path fill="#fff" d="M2 5l6-2 8 3 6-2v15l-6 2-8-3-6 2z"/></svg>USA</span>
    </div>
  </div>

  <div class="card card--about">
    <h2 class="h" style="left:31px;top:25px">About me</h2>
    <p class="para" style="left:31px;top:49px;width:336px">Sed ut perspiciatis unde omnis iste natus error sit voluptatem accusantium doloremque laudantium, totam rem aperiam, eaque ipsa quae ab illo inventore veritatis et quasi architecto beatae vitae dicta sunt explicabo. Nemo enim ipsam voluptatem quia voluptas sit aspernatur aut odit aut fugit, sed quia consequuntur magni dolores eos qui ratione voluptatem uisquaqui dolorem ipsumed ut perspiciatis unde omnis iste natus error sit voluptatem accusantium doloremque laudantium, ue ipsa quae ab illo inventore veritatis ee laudantium, ue ipsa quae ab illo inventore veritatis et quasi architecto beatae vitt expliced ut perspiciatis unde omnis iste natus error sit voluptatem accusantium doloremque laudantium, totam rem aperiam, eaque ipsa quae ab illo inventore veritatis et quasi architecto beatae vitae dicta sunt explicabo. Nemo enim ipsam voluptatem quia voluptas sit aspernatur aut odit aut fugit, sed quia consequuntur magni dolores eos qui ratione voluptatem</p>
    <h2 class="h" style="left:31px;top:178px">Work Experience Overview</h2>
    <table class="xp-table">
      <colgroup><col style="width:79px"><col style="width:154px"><col style="width:106px"></colgroup>
      <tr><th>Role</th><th>Company</th><th>Years of Experience</th></tr>
      <tr><td>Devops Consultant</td><td>Lorem Ipsum dolor sit aptimun Dollhns</td><td>2009-2010</td></tr>
      <tr><td>Cloud Engineer</td><td>Lorem Ipsum dolor sit aptimun Dollhns</td><td>2010-2014</td></tr>
      <tr><td>IT Support Specialist</td><td>Lorem Ipsum dolor sit aptimun Dollhns</td><td>2014-2018</td></tr>
    </table>
  </div>
</section>

<svg width="0" height="0" style="position:absolute">
  <symbol id="tick" viewBox="0 0 10 10"><circle cx="5" cy="5" r="4" fill="none" stroke="#3A3A3A" stroke-width="1.1"/><path d="M3 5.2l1.5 1.4L7.2 3.6" fill="none" stroke="#3A3A3A" stroke-width="1.1"/><path d="M1.5 8.5L8.5 1.5" stroke="#3A3A3A" stroke-width=".8"/></symbol>
</svg>

<!-- Slide 2: experience detail -->
<section class="slide slide--experience">
  <div class="card card--wide">
    <h2 class="h" style="left:36px;top:26px">Professional Experience</h2>
    <div class="role__photo" role="img" aria-label="Small portrait photo of the candidate"></div>
    <div class="role__lines"><strong>Role: Senior Cloud Engineer</strong><br>Company: Lorem Ipsum<br>Timeframe: May 2021 – Present</div>
    <p class="para" style="left:36px;top:114px;width:226px">Sed ut perspiciatis unde omnis iste natus error sit voluptatem accusantium doloremque laudantium, totam rem aperiam, eaque ipsa quae ab illo inventore veritatis et quasi architecto beatae vitae dicta sunt explicabo. Nemo enim ipsam voluptatem quia voluptas sit aspernatur aut odit aut fugit, sed quia consequuntur magni dolores eos qui ratione voluptatem uisquaqui dolorem ipsumed ut perspiciatis unde omnis iste natus error sit voluptatem accusantium doloremque laudantium, ue ipsa quae ab illo inventore veritatis ee laudantium, ue ipsa quae ab illo inventore veritatis et quasi architecto beatae vitt expliced ut perspiciatis unde omnis iste natus error sit voluptatem accusantium doloremque laudantium, totam rem aperiam, eaque ipsa quae ab illo inventore veritatis et quasi architecto beatae vitae dicta sunt explicabo. Nemo enim ipsam voluptatem quia voluptas sit aspernatur aut odit aut fugit, sed quia consequuntur magni dolores eos qui ratione voluptatem</p>
    <div class="divider"></div>

    <h2 class="h" style="left:316px;top:26px">Scope</h2>
    <ul class="list" style="left:318px;top:53px">
      <li><svg><use href="#tick"/></svg>Designed and deployed infrastructure as code using Groundplan</li>
      <li><svg><use href="#tick"/></svg>Implemented security protocols for compliance (ISO 27001)</li>
      <li><svg><use href="#tick"/></svg>Trained internal teams in Nimbus best practices</li>
    </ul>

    <h2 class="h" style="left:316px;top:115px">Achievements</h2>
    <p class="para" style="left:316px;top:138px;width:237px">Veritatis et quasi architecto beatae vitt expliced ut perspiciatis unde omnis iste natus error sit voluptatem accusantium doloremque laudantium, totam rem aperiam, eaquo enim ipsam voluptatem quia voluptas sit aspernatur aut odit aut fugit, sed quia consequuntur</p>

    <svg class="rings" viewBox="0 0 265 92">
      <g fill="none" stroke-width="5">
        <circle cx="46" cy="46" r="42" stroke="var(--ring)"/>
        <circle cx="46" cy="46" r="42" stroke="var(--ring-dark)" stroke-dasharray="76 264" transform="rotate(-90 46 46) scale(1 -1) translate(0 -92)"/>
        <circle cx="131" cy="46" r="42" stroke="var(--ring)"/>
        <circle cx="131" cy="46" r="42" stroke="var(--ring-dark)" stroke-dasharray="125 264" transform="rotate(20 131 46)"/>
        <circle cx="215" cy="46" r="42" stroke="var(--ring)"/>
        <circle cx="215" cy="46" r="42" stroke="var(--ring-dark)" stroke-dasharray="44 264" transform="rotate(-62 215 46)"/>
      </g>
    </svg>
    <div class="ring-label" style="left:358px;top:252px">Reduced<br>deployment<br>time by 60%</div>
    <div class="ring-label" style="left:443px;top:252px">RedImproved<br>system uptime<br>from 95% to<br>99.9%</div>
    <div class="ring-label" style="left:527px;top:252px">Saved<br>€120,000<br>annually via<br>automation</div>
  </div>
  <div class="page-num">02</div>
</section>

<!-- Slide 3: education -->
<section class="slide slide--education">
  <div class="card card--wide">
    <h2 class="h" style="left:36px;top:26px">Education &amp; Competencies</h2>
    <ul class="list" style="left:36px;top:53px">
      <li><svg><use href="#tick"/></svg>BSc in Computer Science – Lorem ipsum dolor sit (2011–2015)</li>
      <li><svg><use href="#tick"/></svg>Cloudforge Certified: Lorem ipsum dolor sit (2022)</li>
      <li><svg><use href="#tick"/></svg>Certified Lorem ipsum dolor sitr (CKA) (2020)</li>
    </ul>
    <h2 class="h" style="left:36px;top:121px">Key Competencies</h2>
    <ul class="list" style="left:36px;top:149px">
      <li><svg><use href="#tick"/></svg>Cloud Architecture (Nimbus, Stratus)</li>
      <li><svg><use href="#tick"/></svg>CI/CD &amp; DevOps Practices</li>
      <li><svg><use href="#tick"/></svg>Infrastructure as Code (Groundplan, Relaywise)</li>
      <li><svg><use href="#tick"/></svg>Security &amp; Compliance (ISO 27001, GDPR)</li>
      <li><svg><use href="#tick"/></svg>Agile &amp; Scrum Methodologies</li>
      <li><svg><use href="#tick"/></svg>Stakeholder Communication</li>
      <li><svg><use href="#tick"/></svg>Systems Integration</li>
    </ul>
    <div class="divider"></div>

    <h2 class="h" style="left:319px;top:26px">Certifications</h2>
    <div class="cert" style="left:319px;top:60px"><div class="cert__sheet" role="img" aria-label="Certificate document"></div></div>
    <div class="cert" style="left:439px;top:60px"><div class="cert__sheet" role="img" aria-label="Certificate document"></div></div>
    <div class="cert" style="left:319px;top:152px"><div class="cert__sheet" role="img" aria-label="Certificate document"></div></div>
    <div class="cert" style="left:439px;top:152px"><div class="cert__sheet" role="img" aria-label="Certificate document"></div></div>
  </div>
  <div class="page-num">03</div>
</section>

</body>
</html>
```